Construction APP

We need to design a modern app IOS/Android where my team can create a profile with their info, (maybe share some pictures), reviews, submit time cards, show their availability, etc.

Like a taxi app but for construction. We also want to be able to assign each team member to a project manager with who they currently working. So we will also need to be able to create profiles at the Administration level.

The goal is to keep innovating the app as we grow, so we are always open to suggestions and ideas.

Low design quality

Industry/Entity Type

Construction

Colors
FFC000
F8CF3A
FAE287
FDF2CF
FEFAEE

Requirements
Must have
• IOS/Android APP where my team can create a profile with their info, (maybe share some pictures), reviews, submit time cards, show their availability, etc.We also want to be able to assign each team member to a project manager with who they currently working. So we will also need to be able to create profiles at the Administration level.

```html
<!DOCTYPE html>
<html lang="en">
<head>
<meta charset="utf-8">
<title>Stoneway Builders – App Screens</title>
<link rel="stylesheet" href="https://fonts.googleapis.com/css2?family=Roboto:wght@400;500;700&display=swap">
<style>
  :root{
    --yellow:#ffc000;
    --gold:#f8cf3a;
    --ink:#111111;
    --text:#1e1e1e;
    --muted:#6f6f6f;
    --soft:#a3a3a3;
    --panel:#eef0f4;
    --field:#eceef2;
    --white:#ffffff;
    --stage:#141414;
    --orange:#e8a400;
  }
  *{box-sizing:border-box;margin:0;padding:0}
  html,body{width:1200px;height:777px;overflow:hidden}
  body{background:var(--stage);font-family:"Roboto",Arial,sans-serif;color:var(--text);position:relative}
  .screen{position:absolute;top:105px;width:261px;height:565px;border-radius:30px;background:var(--white);overflow:hidden}
  .screen--login{left:103px}
  .screen--booking{left:470px;background:var(--panel)}
  .screen--profile{left:836px;background:var(--panel)}
  .status{position:absolute;top:0;left:0;right:0;height:26px;display:flex;align-items:center;justify-content:space-between;padding:0 14px 0 14px;font-size:9px;font-weight:500}
  .status__icons{display:flex;gap:3px;align-items:center}
  .appbar{position:absolute;top:0;left:0;right:0;height:73px;background:var(--white)}
  .appbar__title{position:absolute;top:37px;left:0;right:0;text-align:center;font-size:14px;font-weight:500}
  .appbar__back{position:absolute;left:15px;top:40px}
  .appbar__menu{position:absolute;left:223px;top:34px;width:24px;height:24px;border-radius:50%;background:#e3e5e9;display:flex;align-items:center;justify-content:center}

  /* login */
  .brand{position:absolute;top:82px;left:0;right:0;display:flex;justify-content:center;align-items:center;gap:6px;font-size:17px;font-weight:700;color:var(--ink);letter-spacing:.3px}
  .brand__dot{width:10px;height:10px;border-radius:50%;background:var(--yellow)}
  .services{position:absolute;left:14px;top:163px;font-size:11px}
  .services__lead{color:var(--muted);margin-bottom:6px}
  .services__list{font-weight:500}
  .label{position:absolute;left:14px;font-size:10.5px;font-weight:500}
  .input{position:absolute;left:14px;width:234px;height:36px;background:var(--white);box-shadow:0 3px 10px rgba(0,0,0,.08);border:1px solid #eee;font-size:8.5px;color:var(--muted);display:flex;align-items:center;padding-left:16px}
  .btn{position:absolute;top:424px;height:32px;border-radius:16px;display:flex;align-items:center;justify-content:center;font-size:10px;font-weight:700}
  .btn--dark{left:14px;width:126px;background:var(--ink);color:var(--white)}
  .btn--yellow{left:148px;width:98px;background:var(--yellow);color:var(--white)}
  .signup{position:absolute;top:488px;left:0;right:0;text-align:center;font-size:10px;color:var(--muted)}
  .signup b{color:var(--ink);font-weight:500}

  /* booking */
  .worker{position:absolute;left:14px;width:234px;height:71px;background:var(--white);border-radius:3px}
  .worker__photo{position:absolute;left:6px;top:10px;width:52px;height:52px;border-radius:50%;background:linear-gradient(135deg,#d7c46a,#5d7890)}
  .worker__name{position:absolute;left:68px;top:14px;font-size:11.5px;font-weight:500}
  .worker__role{position:absolute;left:68px;top:31px;font-size:7.5px;color:var(--orange)}
  .worker__rating{position:absolute;left:70px;top:44px;font-size:7.5px;color:var(--muted);display:flex;gap:1px;align-items:center}
  .worker__rating span{color:var(--yellow)}
  .worker__book{position:absolute;left:156px;top:25px;width:71px;height:21px;border-radius:11px;background:var(--yellow);color:var(--white);font-size:9.5px;font-weight:500;display:flex;align-items:center;justify-content:center}

  /* profile */
  .profile-card{position:absolute;left:14px;top:89px;width:234px;height:490px;background:var(--white)}
  .profile-photo{position:absolute;left:94px;top:16px;width:71px;height:71px;border-radius:50%;background:linear-gradient(135deg,#9fb3c4,#2f3a46)}
  .profile-name{position:absolute;top:99px;left:0;right:0;text-align:center;font-size:14px;font-weight:500}
  .profile-role{position:absolute;top:119px;left:0;right:0;text-align:center;font-size:9.5px;color:var(--orange)}
  .field{position:absolute;left:21px;width:219px;height:34px;border-radius:17px;background:var(--field);display:flex;align-items:center;justify-content:space-between;padding:0 15px;font-size:11.5px;color:#8d8d8d}
  .book-now{position:absolute;left:21px;top:504px;width:219px;height:34px;border-radius:17px;background:var(--yellow);color:var(--white);font-size:12.5px;font-weight:700;display:flex;align-items:center;justify-content:center;box-shadow:0 6px 12px rgba(255,192,0,.35)}
</style>
</head>
<body>

<svg width="0" height="0" style="position:absolute">
  <defs>
    <symbol id="icon-signal" viewBox="0 0 12 8"><rect x="0" y="5" width="2" height="3"/><rect x="3" y="3.5" width="2" height="4.5"/><rect x="6" y="2" width="2" height="6"/><rect x="9" y="0" width="2" height="8"/></symbol>
    <symbol id="icon-battery" viewBox="0 0 16 8"><rect x=".5" y=".5" width="13" height="7" rx="1.5" fill="none" stroke="currentColor"/><rect x="2" y="2" width="10" height="4"/><rect x="14.5" y="2.5" width="1.5" height="3"/></symbol>
    <symbol id="icon-back" viewBox="0 0 16 8"><path d="M1 4h15M1 4l4-3.5M1 4l4 3.5" stroke="currentColor" stroke-width="1.8" fill="none"/></symbol>
    <symbol id="icon-menu" viewBox="0 0 10 8"><path d="M0 1h10M0 4h10M0 7h10" stroke="currentColor" stroke-width="1.4"/></symbol>
    <symbol id="icon-pencil" viewBox="0 0 10 10"><path d="M1 9l1-3 5-5 2 2-5 5z" fill="currentColor"/></symbol>
    <symbol id="icon-caret" viewBox="0 0 8 4"><path d="M0 0h8L4 4z" fill="currentColor"/></symbol>
  </defs>
</svg>

<!-- Login -->
<section class="screen screen--login">
  <div class="status">
    <span>09:41</span>
    <span class="status__icons"><svg width="10" height="7"><use href="#icon-signal"/></svg><svg width="14" height="7" style="color:#111"><use href="#icon-battery"/></svg></span>
  </div>
  <div class="brand"><span class="brand__dot"></span>STONEWAY BUILDERS</div>
  <div class="services">
    <p class="services__lead">Construction</p>
    <p class="services__list">Home Improvement &nbsp;| &nbsp;Electrical Services</p>
  </div>
  <p class="label" style="top:235px">Email Address</p>
  <div class="input" style="top:252px">Email Address</div>
  <p class="label" style="top:321px">Password</p>
  <div class="input" style="top:338px">Enter Your Password</div>
  <div class="btn btn--dark">FORGOT PASSWORD</div>
  <div class="btn btn--yellow">LOGIN ME</div>
  <p class="signup">Don't have a account? &nbsp;<b>Membership</b></p>
</section>

<!-- Booking -->
<section class="screen screen--booking">
  <div class="appbar">
    <div class="status"><span>12:00</span><span class="status__icons"><svg width="10" height="7"><use href="#icon-signal"/></svg><svg width="14" height="7"><use href="#icon-battery"/></svg></span></div>
    <svg class="appbar__back" width="16" height="8"><use href="#icon-back"/></svg>
    <h1 class="appbar__title">Booking</h1>
    <span class="appbar__menu"><svg width="10" height="8"><use href="#icon-menu"/></svg></span>
  </div>
  <article class="worker" style="top:105px"><div class="worker__photo" role="img" aria-label="Photo of a construction worker in a hard hat"></div><p class="worker__name">Marco Diaz</p><p class="worker__role">civil engineer</p><p class="worker__rating"><span>★★★★★</span>&nbsp;(320)</p><span class="worker__book">Book Now</span></article>
  <article class="worker" style="top:191px"><div class="worker__photo" role="img" aria-label="Photo of a construction worker in a hard hat"></div><p class="worker__name">Marco Diaz</p><p class="worker__role">civil engineer</p><p class="worker__rating"><span>★★★★★</span>&nbsp;(320)</p><span class="worker__book">Book Now</span></article>
  <article class="worker" style="top:277px"><div class="worker__photo" role="img" aria-label="Photo of a construction worker in a hard hat"></div><p class="worker__name">Marco Diaz</p><p class="worker__role">civil engineer</p><p class="worker__rating"><span>★★★★★</span>&nbsp;(320)</p><span class="worker__book">Book Now</span></article>
  <article class="worker" style="top:362px"><div class="worker__photo" role="img" aria-label="Photo of a construction worker in a hard hat"></div><p class="worker__name">Marco Diaz</p><p class="worker__role">civil engineer</p><p class="worker__rating"><span>★★★★★</span>&nbsp;(320)</p><span class="worker__book">Book Now</span></article>
  <article class="worker" style="top:448px"><div class="worker__photo" role="img" aria-label="Photo of a construction worker in a hard hat"></div><p class="worker__name">Marco Diaz</p><p class="worker__role">civil engineer</p><p class="worker__rating"><span>★★★★★</span>&nbsp;(320)</p><span class="worker__book">Book Now</span></article>
</section>

<!-- Profile -->
<section class="screen screen--profile">
  <div class="appbar">
    <div class="status"><span>12:00</span><span class="status__icons"><svg width="10" height="7"><use href="#icon-signal"/></svg><svg width="14" height="7"><use href="#icon-battery"/></svg></span></div>
    <svg class="appbar__back" width="16" height="8"><use href="#icon-back"/></svg>
    <h1 class="appbar__title">Profile</h1>
    <span class="appbar__menu"><svg width="10" height="8"><use href="#icon-menu"/></svg></span>
  </div>
  <div class="profile-card">
    <div class="profile-photo" role="img" aria-label="Profile photo of an engineer on a construction site"></div>
    <h2 class="profile-name">Owen Hartley</h2>
    <p class="profile-role">civil engineer</p>
  </div>
  <div class="field" style="top:247px">Owen Hartley<svg width="9" height="9" style="color:#bbb"><use href="#icon-pencil"/></svg></div>
  <div class="field" style="top:295px">+800 555 010 2030<svg width="9" height="9" style="color:#bbb"><use href="#icon-pencil"/></svg></div>
  <div class="field" style="top:342px">name@stoneway.build<svg width="9" height="9" style="color:#bbb"><use href="#icon-pencil"/></svg></div>
  <div class="field" style="top:389px">Submit time cards<svg width="7" height="4" style="color:#aaa"><use href="#icon-caret"/></svg></div>
  <div class="field" style="top:436px">Available<svg width="7" height="4" style="color:#aaa"><use href="#icon-caret"/></svg></div>
  <div class="book-now">BOOK NOW</div>
</section>

</body>
</html>
```